Q.R. Bright Desk Store

The design is for eCommerce home page but I would like it to complement this site: http://www.qrbrightdesksystems.com/ but... it should also have independence as a standalone site.

The best design will be able to effectively mix corporate with a high quality small business consumer feel. It should be completely custom design, not a template look or feel. I want the users to get the feeling that this is the place to go for buying tech for business. We sell the same products as Vantrel.

You can be creative as you wish, as long as the elements of a great eCommerce site are present.

I would like your 'design' to blow these away:
http://www.buying.zorvex.com/
mivoland.com
http://www.vantrel.com/

Here are references:
Call to action
http://trabelwise.com/us/blog/48173-seven-tips-for-designing-an-effective-ecommerce-call-to-action

Effective Ecommerce design
http://www.plov.com/ss/7-tips-for-effective-e-commerce#0

91 points of ecommerce
http://dreb.com/blog/holygrail-of-ecommerce-conversion-optimization-91-points-checklist

UPDATE 07/11/2013:

Please look at the category sample png files. I see already many people are using the main menu from qrbrightdesksystems.com and I do not mind your creativiety, but this is an eCommerce store and people need a menu to get to the categories and/or product types. I don't want to limit anyone creativity by the png samples. I'm also not using them to show I like them in any particular way or form, just that it's needed, whether it's a button (dropdown of course) that says 'Categories' or 'Products, whether it an accordion, horizontal or vertical.

Thanks

UPDATE 07/12/2013:

Please find other use of space that has been used for About Us paragraph (if you've added it to the page). About Us should have it's own page and the purpose of the design should be to sell products (and some services as products). Please put a link or some other creative method to lead users to the About Us page.

Reason: I've raised the award, including 1st, 2nd, and 3rd place and participation payments so I will also extend 7 days. Thanks!

I've updated the product brief. Please scroll down to where it says: UPDATE 07/11/2013

Thanks!

UPDATE 07/12/2013:

Please find other use of space that has been used for About Us paragraph (if you've added it to the page).  About Us should have it's own page and the purpose of the design should be to sell products (and some services as products). Please put a link or some other creative method to lead users to the About Us page if you must but not on the real estate of the page.

Thanks!

Added updates to the brief 7/14/2013.

Thanks!

The voting is in and the project is complete.  Thanks everyone for joining, all of those who participated are truly amazingly talented. But, there were only 3 prizes.  I will be having further projects down the line to develop other pages to this site after the initial implementation is completed.  I truly would like to have you all back. 

- Thank you.

Target Market(s)

corporate decision-makers AND small business consumers

Industry/Entity Type

Small Business

Requirements
Must have
• Call to action.
Openness (non-clutter).

These elements:
Search box
Logo
Tagline
Telephone number
Contact details
Address
My account / sign in
Shopping basket / checkout link
Latest offers
Promotional area
Email sign up
Delivery information
About us
Link to press office / corporate site
Terms and conditions
Sitemap for the footer.
Delivery offers: free
Personalized recommendations
Social media links
Accepted payment methods
Link to blog or community section
Change language / country

http://freshnotesblog.kelvarant.com/sales-leads-landing-page/

UPDATE 07/14/2013
Category Menu. This can be a dropdown, horizontal, vertical, etc. But shoppers need to know how to get to the products they want to buy.
Nice to have
• Trustmarks
Blog/Blog link

UPDATE 07/12/2013:
Make the footer useful.

UPDATE 07/14/2013 (Suggestions of elements to differentiate your designs)

-Quick Shop: A quick buy module/section: Where a user can put in a SKU number or Model number to quickly add the product to their shopping cart.

-Featured
-Best Sellers
-Specials
-Trending Tags/Tag Cloud
- Activity Stream
- Cross Sell/ Up Sell
- Testimonial
- Social Network Feed
- Live Help
- Feedback/Support/Contact Tab
- Show logged in user (i.e. Welcome, Mark Pell)
Should not have
• The design SHOULD NOT be generic like this:

http://www.artflock.com/design/52392
http://www.pelicanvault.com/

The page should not feel over cluttered. It should not have low quality icons or design elements. Navigation should not be hard to discover or confusing.

```html
<!DOCTYPE html>
<html lang="en">
<head>
<meta charset="utf-8">
<title>Q.R. Bright Desk – Hardware</title>
<link href="https://fonts.googleapis.com/css2?family=Open+Sans:wght@400;600&display=swap" rel="stylesheet">
<style>
:root{
  --orange:#f7923a;
  --orange-dark:#e8761d;
  --blue:#3a8bc4;
  --blue-dark:#2f79ad;
  --blue-light:#a9c9e2;
  --grey-bar:#d2d2d2;
  --grey-side:#575757;
  --grey-side-dark:#474747;
  --dark:#3a3a3a;
  --footer:#2c2c2c;
  --footer-head:#232323;
  --footer-bottom:#1b1b1b;
  --text:#444;
  --muted:#9a9a9a;
  --white:#fff;
}
*{box-sizing:border-box;margin:0;padding:0}
html,body{width:1089px;height:1200px;overflow:hidden}
body{font-family:"Open Sans",Arial,sans-serif;color:var(--text);background:#f4f4f4;font-size:12px}
a{color:inherit;text-decoration:none}
.wrap{width:858px;margin-left:108px;position:relative}

/* top bar */
.topbar{height:32px;background:var(--grey-bar)}
.topbar .wrap{height:32px;display:flex;align-items:center;justify-content:space-between}
.langs{display:flex;gap:4px;margin-left:15px}
.langs span{width:11px;height:8px;display:block}
.social{display:flex}
.social span{width:32px;height:27px;display:block;margin-top:-5px}
.s-a{background:#3b5998}.s-b{background:#6fcbe8}.s-c{background:#f28a22}
.account{display:flex;align-items:center;gap:20px;font-size:12px;color:#333;white-space:nowrap}
.account nav{display:flex;gap:8px}
.account nav i{font-style:normal;color:#666}

/* header */
.header{height:83px;background:var(--white)}
.header .wrap{height:83px;display:flex;align-items:center}
.brand{display:flex;align-items:center;gap:7px;padding-left:6px}
.brand-dot{width:40px;height:40px;border-radius:50%;background:var(--blue-dark)}
.brand-name{font-size:19px;color:var(--blue-dark);line-height:1.05;white-space:nowrap}
.tagline{margin-left:18px;padding-left:15px;border-left:1px solid #e2e2e2;height:52px;display:flex;align-items:center;color:var(--blue);font-size:16px;white-space:nowrap}
.help{margin-left:auto;text-align:left;white-space:nowrap}
.help h2{font-size:20px;font-weight:400;color:var(--orange)}
.help-row{display:flex;gap:10px;align-items:center}
.phone-icon{width:40px;height:38px;background:var(--orange);display:flex;align-items:center;justify-content:center}
.help-row p{font-size:15px;line-height:19px;color:#333}
.help-row b{font-weight:600}

/* main nav */
.mainnav{height:43px;background:var(--blue)}
.mainnav .wrap{display:flex;height:43px}
.mainnav a{flex:none;display:flex;align-items:center;gap:10px;color:var(--white);font-size:14.5px;padding:0 0 0 14px;border-right:1px solid var(--blue-dark);height:43px;white-space:nowrap}
.mainnav a.active{background:var(--blue-light);color:#333}
.mainnav .n-hw{width:119px}
.mainnav .n-sw{width:111px;padding-left:22px}
.mainnav .n-it{width:141px;padding-left:22px}
.mainnav .n-te{width:132px;padding-left:22px}
.caret{width:0;height:0;border-left:4px solid transparent;border-right:4px solid transparent;border-top:5px solid currentColor}
.mainnav .basket{width:193px;gap:18px;padding-left:22px;font-size:15.5px}
.mainnav .items{width:162px;border:0;gap:6px;padding-left:22px;font-size:15.5px}
.items .count{color:var(--orange)}

/* hero */
.hero{height:138px;background:var(--dark);padding-top:7px}
.hero-banner{height:120px;width:858px;margin-left:110px;position:relative;background:linear-gradient(120deg,#1f5d3e,#5fb184 45%,#2c7a52 70%,#6fc296)}
.hero-title{position:absolute;left:13px;top:20px;width:328px;height:86px;background:rgba(0,0,0,.88);color:var(--white);font-size:52px;line-height:86px;padding-left:45px;white-space:nowrap}
.hero-offer{position:absolute;left:535px;top:9px;width:309px;height:98px;background:#bdbdbd;color:var(--white);font-size:20px;display:flex;align-items:center;justify-content:center}

/* content */
.content{height:614px;background:var(--white);position:relative}
.main{position:absolute;left:110px;top:0;width:651px}
.crumbs{height:44px;background:var(--blue);display:flex;align-items:center;padding-left:18px;color:var(--white);font-size:15px;gap:6px}
.crumbs a{text-decoration:underline}
.views{margin-left:auto;display:flex;height:44px}
.views span{width:40px;height:44px;display:flex;align-items:center;justify-content:center}
.views span:first-child{background:var(--blue-light)}
.pager-row{height:38px;display:flex;align-items:center;justify-content:space-between;padding:0 15px 0 3px;font-size:12.5px}
.pager-row em{font-style:normal;color:var(--orange);text-decoration:underline}
.grid{display:grid;grid-template-columns:repeat(3,213px);gap:11px 7px}
.card{height:218px;border:1px solid #eee;display:flex;flex-direction:column}
.card h3{height:37px;background:var(--orange);color:var(--white);font-weight:600;font-size:14px;text-align:center;line-height:37px;white-space:nowrap}
.card .pic{flex:1;margin:10px auto;width:150px;background:linear-gradient(#e9e9e9,#cfcfcf)}
.card .buy{height:46px;background:#f6f6f6;display:flex;align-items:center;justify-content:space-between;padding:0 6px 0 8px;white-space:nowrap}
.price{color:var(--muted);font-size:14px;line-height:14px}
.price b{font-weight:400;color:var(--blue)}
.price small{font-size:12px;display:block}
.price s{color:#777}
.show{display:flex;height:32px;background:var(--blue);color:var(--white);font-size:14px;align-items:center}
.show span{padding:0 11px}
.show i{width:29px;height:32px;background:var(--blue-dark);display:flex;align-items:center;justify-content:center}
.pager-row.bottom{margin-top:21px;border-top:1px solid #e8e8e8;border-bottom:1px solid #e8e8e8}

/* sidebar */
.side{position:absolute;left:767px;top:0;width:199px}
.search{height:46px;background:var(--grey-side);display:flex;align-items:center;padding:0 7px}
.search span{flex:1;height:31px;background:var(--white);color:#888;font-size:11.5px;padding-left:13px;line-height:31px}
.search i{width:36px;display:flex;justify-content:center}
.cats{margin-top:6px;border:2px solid var(--orange);border-top:0;background:var(--grey-side)}
.tabs{height:42px;display:flex;background:var(--orange);color:var(--white);font-size:18px;align-items:flex-end}
.tabs span{padding:0 14px 6px 14px}
.tabs .off{background:var(--orange-dark);height:42px;margin-left:auto;line-height:40px;padding:0 14px}
.cat-head{height:38px;display:flex;align-items:center;justify-content:space-between;padding:0 12px 0 17px;color:var(--white);font-size:16px}
.cat-head.open{background:var(--blue);border-top:2px solid var(--grey-side)}
.cat-head.closed{background:var(--grey-side-dark);border-top:1px solid #3a3a3a;height:37px}
.up{border-left:4px solid transparent;border-right:4px solid transparent;border-bottom:5px solid var(--white)}
.dn{border-left:4px solid transparent;border-right:4px solid transparent;border-top:5px solid var(--white)}
.sub{list-style:none;padding:4px 0 2px 30px}
.sub li{height:27.5px;line-height:27.5px;color:#eee;font-size:12.5px}
.side-btn{margin-top:7px;height:43px;color:var(--white);font-size:18px;padding-left:17px;line-height:43px}
.side-btn.orange{background:var(--orange);margin-top:6px}
.side-btn.blue{background:var(--blue);margin-top:5px}
.more{margin:6px 0 0 32px;height:29px;background:#bdbdbd;color:var(--white);font-size:13px;display:flex;align-items:center;justify-content:space-between;padding:0 12px 0 24px}

/* footer */
.footer{height:238px;background:var(--footer);color:#eee}
.footer-head{height:51px;background:var(--footer-head)}
.fcols{position:absolute;top:0;left:0;width:858px;display:grid;grid-template-columns:222px 212px 218px 206px}
.fcol h4{height:51px;line-height:51px;font-weight:400;font-size:18px;color:var(--white);padding-left:9px;white-space:nowrap}
.links{list-style:none;margin:5px 16px 0 9px}
.links li{height:26px;line-height:26px;padding-left:11px;border-bottom:1px solid #444;font-size:12px}
.links li:last-child{border:0}
.fcol p{font-size:11.5px;line-height:17px;padding:10px 14px 0 11px}
.fcol p.one{white-space:nowrap;padding-right:0}
.email{margin:14px 0 0 10px;width:187px;height:31px;display:flex;border:2px solid #ddd;background:var(--white)}
.email span{flex:1;color:#333;font-size:12.5px;line-height:27px;padding-left:9px}
.email i{width:26px;background:#444;display:flex;align-items:center;justify-content:center}
.cards{display:grid;grid-template-columns:repeat(4,43px);gap:5px 4px;padding:12px 0 0 11px}
.cards span{height:25px;border-radius:2px;display:block}
.fcol .contact{font-size:10.5px;line-height:17px;padding:10px 20px 0 9px}
.stay{font-size:16px;color:var(--white);padding:10px 0 0 9px}
.stay-icons{display:flex;gap:4px;padding:4px 0 0 9px}
.stay-icons span{width:23px;height:23px;border-radius:3px}
.bottom-bar{height:52px;background:var(--footer-bottom);color:#eee;font-size:11px}
.bottom-bar .wrap{height:52px;display:flex;align-items:center;justify-content:flex-end;padding-right:14px}
</style>
</head>
<body>

<div class="topbar">
  <div class="wrap">
    <div class="langs">
      <span style="background:#d8a200"></span><span style="background:#2a4fa3"></span><span style="background:#c8102e"></span>
    </div>
    <div class="account">
      <div class="social"><span class="s-a"></span><span class="s-b"></span><span class="s-c"></span></div>
      <nav><a>My account</a><i>|</i><a>sign in</a><i>|</i><a>Register</a></nav>
    </div>
  </div>
</div>

<header class="header">
  <div class="wrap">
    <div class="brand">
      <span class="brand-dot"></span>
      <span class="brand-name">Q.R. Bright Desk</span>
    </div>
    <div class="tagline">Tag line goes here</div>
    <div class="help">
      <h2>We're Here to Help!</h2>
      <div class="help-row">
        <div class="phone-icon">
          <svg width="22" height="22" viewBox="0 0 24 24"><path fill="#fff" d="M6.6 10.8c1.4 2.8 3.8 5.1 6.6 6.6l2.2-2.2c.3-.3.7-.4 1-.2 1.1.4 2.3.6 3.6.6.6 0 1 .4 1 1V20c0 .6-.4 1-1 1C10.6 21 3 13.4 3 4c0-.6.4-1 1-1h3.5c.6 0 1 .4 1 1 0 1.3.2 2.5.6 3.6.1.3 0 .7-.2 1z"/></svg>
        </div>
        <p><b>LCL:</b> 212 555 0148<br><b>TF:</b> 888 555 0192</p>
      </div>
    </div>
  </div>
</header>

<nav class="mainnav">
  <div class="wrap">
    <a class="n-hw active">Hardware <span class="caret" style="color:#888"></span></a>
    <a class="n-sw">Software <span class="caret"></span></a>
    <a class="n-it">IT Resources <span class="caret"></span></a>
    <a class="n-te">Technology <span class="caret"></span></a>
    <a class="basket">
      <svg width="30" height="22" viewBox="0 0 30 22"><path d="M1 2h5l4 12h14l3-9H8" fill="none" stroke="#fff" stroke-width="2.5"/><circle cx="12" cy="19" r="2" fill="#fff"/><circle cx="22" cy="19" r="2" fill="#fff"/></svg>
      My Basket <span class="caret"></span>
    </a>
    <a class="items"><span class="count">0 items</span> : £0.00</a>
  </div>
</nav>

<section class="hero">
  <div class="hero-banner" role="img" aria-label="Close-up of a green circuit board">
    <div class="hero-title">Hardware</div>
    <div class="hero-offer">SPECIAL OFFERS</div>
  </div>
</section>

<main class="content">
  <div class="main">
    <div class="crumbs">
      <a>Home</a> - <span>Harware</span>
      <div class="views">
        <span><svg width="26" height="26" viewBox="0 0 26 26" fill="none" stroke="#fff" stroke-width="1.5"><rect x="1" y="1" width="6" height="6"/><rect x="10" y="1" width="6" height="6"/><rect x="19" y="1" width="6" height="6"/><rect x="1" y="10" width="6" height="6"/><rect x="10" y="10" width="6" height="6"/><rect x="19" y="10" width="6" height="6"/><rect x="1" y="19" width="6" height="6"/><rect x="10" y="19" width="6" height="6"/><rect x="19" y="19" width="6" height="6"/></svg></span>
        <span><svg width="26" height="26" viewBox="0 0 26 26" fill="#2a6f9f"><rect x="0" y="0" width="5" height="5"/><rect x="7" y="0" width="5" height="5"/><rect x="14" y="0" width="5" height="5"/><rect x="21" y="0" width="5" height="5"/><rect x="0" y="7" width="5" height="5"/><rect x="7" y="7" width="5" height="5"/><rect x="14" y="7" width="5" height="5"/><rect x="21" y="7" width="5" height="5"/><rect x="0" y="14" width="5" height="5"/><rect x="7" y="14" width="5" height="5"/><rect x="14" y="14" width="5" height="5"/><rect x="21" y="14" width="5" height="5"/><rect x="0" y="21" width="5" height="5"/><rect x="7" y="21" width="5" height="5"/><rect x="14" y="21" width="5" height="5"/><rect x="21" y="21" width="5" height="5"/></svg></span>
      </div>
    </div>
    <div class="pager-row"><span>View <em>80</em> products per page</span><span>1 &nbsp;<em>2</em>&nbsp; Next</span></div>

    <div class="grid">
      <article class="card"><h3>Product name</h3><div class="pic" role="img" aria-label="Flat screen monitor"></div>
        <div class="buy"><p class="price">Only <b>£300.00</b></p><a class="show"><span>Show me</span><i><svg width="12" height="12" viewBox="0 0 12 12"><circle cx="6" cy="6" r="6" fill="#fff"/><path d="M6 3v6M3 6h6" stroke="#2f79ad" stroke-width="2"/></svg></i></a></div></article>
      <article class="card"><h3>Product with a long name</h3><div class="pic" role="img" aria-label="Grey and red headphones"></div>
        <div class="buy"><p class="price">Only <b>£99.00</b></p><a class="show"><span>Show me</span><i><svg width="12" height="12" viewBox="0 0 12 12"><circle cx="6" cy="6" r="6" fill="#fff"/><path d="M6 3v6M3 6h6" stroke="#2f79ad" stroke-width="2"/></svg></i></a></div></article>
      <article class="card"><h3>Product name</h3><div class="pic" role="img" aria-label="Black laptop"></div>
        <div class="buy"><p class="price"><small>Was <s>£9999.00</s></small>Now <b>£999.00</b></p><a class="show"><span>Show me</span><i><svg width="12" height="12" viewBox="0 0 12 12"><circle cx="6" cy="6" r="6" fill="#fff"/><path d="M6 3v6M3 6h6" stroke="#2f79ad" stroke-width="2"/></svg></i></a></div></article>
      <article class="card"><h3>Product name</h3><div class="pic" role="img" aria-label="Flat screen monitor"></div>
        <div class="buy"><p class="price">Only <b>£300.00</b></p><a class="show"><span>Show me</span><i><svg width="12" height="12" viewBox="0 0 12 12"><circle cx="6" cy="6" r="6" fill="#fff"/><path d="M6 3v6M3 6h6" stroke="#2f79ad" stroke-width="2"/></svg></i></a></div></article>
      <article class="card"><h3>Product with a long name</h3><div class="pic" role="img" aria-label="Grey and red headphones"></div>
        <div class="buy"><p class="price">Only <b>£99.00</b></p><a class="show"><span>Show me</span><i><svg width="12" height="12" viewBox="0 0 12 12"><circle cx="6" cy="6" r="6" fill="#fff"/><path d="M6 3v6M3 6h6" stroke="#2f79ad" stroke-width="2"/></svg></i></a></div></article>
      <article class="card"><h3>Product name</h3><div class="pic" role="img" aria-label="Black laptop"></div>
        <div class="buy"><p class="price"><small>Was <s>£9999.00</s></small>Now <b>£999.00</b></p><a class="show"><span>Show me</span><i><svg width="12" height="12" viewBox="0 0 12 12"><circle cx="6" cy="6" r="6" fill="#fff"/><path d="M6 3v6M3 6h6" stroke="#2f79ad" stroke-width="2"/></svg></i></a></div></article>
    </div>

    <div class="pager-row bottom"><span>View <em>80</em> products per page</span><span>1 &nbsp;<em>2</em>&nbsp; Next</span></div>
  </div>

  <aside class="side">
    <div class="search"><span>Product search</span><i><svg width="22" height="22" viewBox="0 0 22 22" fill="none" stroke="#fff" stroke-width="2"><circle cx="13" cy="9" r="7"/><path d="M8 14l-6 6"/></svg></i></div>
    <div class="cats">
      <div class="tabs"><span>Categories</span><span class="off">Filters</span></div>
      <div class="cat-head open">Hardware <span class="up"></span></div>
      <ul class="sub">
        <li>Desktops</li><li>Laptops &amp; Notebooks</li><li>Components</li><li>Tablets</li><li>Software</li><li>Phones &amp; PDAs</li><li>Cameras</li><li>MP3 Players</li>
      </ul>
      <div class="cat-head closed">Software <span class="dn"></span></div>
      <div class="cat-head closed">IT Resources <span class="dn"></span></div>
      <div class="cat-head closed">Technology <span class="dn"></span></div>
    </div>
    <a class="side-btn orange" style="display:block">My Account</a>
    <a class="side-btn blue" style="display:block">Contact us</a>
    <a class="more">More information <span class="dn"></span></a>
  </aside>
</main>

<footer class="footer">
  <div class="footer-head"></div>
  <div class="wrap" style="margin-top:-51px">
    <div class="fcols">
      <div class="fcol">
        <h4>Quick links</h4>
        <ul class="links"><li>Shop</li><li>Latest offers</li><li>Shopping basket</li><li>Press office / corporate site</li><li>Terms and conditions</li><li>Sitemap</li></ul>
      </div>
      <div class="fcol">
        <h4>Email Sign up</h4>
        <p>Keep up-to-date with all of our latest products and special offers</p>
        <p style="padding-top:12px">Sign up to our newsletter</p>
        <div class="email"><span>Email address</span><i><svg width="6" height="8" viewBox="0 0 6 8"><path d="M0 0l6 4-6 4z" fill="#fff"/></svg></i></div>
      </div>
      <div class="fcol">
        <h4>Payment options</h4>
        <p class="one">We accept all of the payments below</p>
        <div class="cards">
          <span style="background:#1a3f8f"></span><span style="background:#e3e3e3"></span><span style="background:#1a5fa8"></span><span style="background:#f2f2f2"></span>
          <span style="background:#3f8fd1"></span><span style="background:#dcdcdc"></span><span style="background:#f4f4f4"></span><span style="background:#1b4f95"></span>
        </div>
      </div>
      <div class="fcol">
        <h4>Contact details</h4>
        <p class="contact">Lorem ipsum dolor sit amet, consectetur adipiscing elit. Proin aliquet, enim quis sagittis rutrum, purus metus posuere nibh, sit</p>
        <p class="contact" style="padding-top:12px">info@qrbrightdesksystems.com</p>
        <div class="stay">Stay in touch</div>
        <div class="stay-icons"><span class="s-a"></span><span class="s-b"></span><span class="s-c"></span></div>
      </div>
    </div>
  </div>
</footer>

<div class="bottom-bar"><div class="wrap">Copyright 2013 · All rights reserved</div></div>

</body>
</html>
```